Chiropractic healthcare group business card

We are a Portland Oregon based chiropractic healthcare group. Looking for a new business card design. Something cutting edge, that shows off our new logo and tag line.Use either of the attached logos.Our tag line = "Move freely, live fully again!"I'm open to about anything, impress me!!
Target Market(s)
Chiropractic patients - Auto injury, back pain, sports injuries, neck , shoulder, hip, knee, ankle pain.
Industry/Entity Type
Chiropractic
Contact Information for Business Card
Dr. Bram Tovelund, D.C.
Clinic name - Cedar Chiropractic
2 clinics
location #1
20418 NW Harlow Road
Suite 4
Alder Bend, OR 97412
Location #2
13529 SE Marston Street
Fernwick OR 97358
Main phone line 971.386.4217
website : www.BirchValeCare.com
Tag line "Move freely, live fully again!"
Colors
Designer to choose colors to be used in the design.
Requirements
Must have
- Use the logo colors -- Want the orange color to be a TRUE orange.
- Both clinic address
- phone number
- website
- personal email - b.tovelund@FreshStrideHealth.com
- tag line - "Move freely, live fully again!"

```html
<!DOCTYPE html>
<html lang="en">
<head>
<meta charset="utf-8">
<title>Cedar Chiropractic – Business Card</title>
<link href="https://fonts.googleapis.com/css2?family=Oswald:wght@500&family=Roboto:wght@400;500;700&display=swap" rel="stylesheet">
<style>
  :root {
    --orange: #ff8000;
    --charcoal: #4a4d52;
    --slate: #7a7d82;
    --paper: #ffffff;
    --backdrop: #ececec;
  }
  * { box-sizing: border-box; margin: 0; padding: 0; }
  html, body { width: 1200px; height: 760px; overflow: hidden; }
  body {
    background: var(--backdrop);
    font-family: "Roboto", Arial, sans-serif;
    position: relative;
  }
  .card {
    position: absolute;
    top: 230px;
    width: 525px;
    height: 300px;
    overflow: hidden;
    box-shadow: 0 10px 24px rgba(0,0,0,.18);
  }

  /* Front */
  .card-front { left: 55px; background: var(--orange); }
  .brand {
    position: absolute;
    top: 96px; left: 0; right: 0;
    display: flex; align-items: center; justify-content: center; gap: 14px;
  }
  .brand-mark { width: 24px; height: 24px; background: var(--charcoal); flex: none; }
  .brand-name {
    color: var(--charcoal);
    font-weight: 700;
    font-size: 28px;
    letter-spacing: 5px;
    text-transform: uppercase;
    white-space: nowrap;
  }
  .tagline-band {
    position: absolute;
    left: 0; right: 0; top: 206px; height: 50px;
    background: var(--paper);
    display: flex; align-items: center; justify-content: center;
  }
  .tagline {
    font-family: "Oswald", "Arial Narrow", sans-serif;
    font-weight: 500;
    font-size: 30px;
    color: var(--orange);
    text-transform: uppercase;
    white-space: nowrap;
  }

  /* Back */
  .card-back { left: 620px; background: var(--paper); }
  .contact { position: absolute; left: 32px; top: 38px; }
  .doctor-name { color: var(--orange); font-weight: 700; font-size: 19px; margin-bottom: 22px; }
  .contact-list { list-style: none; color: var(--charcoal); font-size: 12px; line-height: 16px; }
  .contact-list li { display: flex; align-items: center; gap: 6px; }
  .contact-list svg { width: 11px; height: 11px; flex: none; }
  .clinic { margin-top: 20px; font-size: 12px; line-height: 15px; color: var(--charcoal); }
  .clinic-title { color: var(--orange); }
  .clinic-rule { width: 78px; height: 1px; background: var(--charcoal); margin: 6px 0 5px; }
  .corner-band {
    position: absolute;
    right: 0; bottom: 0; width: 190px; height: 100px;
  }
</style>
</head>
<body>
  <section class="card card-front">
    <div class="brand">
      <span class="brand-mark"></span>
      <span class="brand-name">Cedar Chiropractic</span>
    </div>
    <div class="tagline-band">
      <p class="tagline">Move freely, live fully again!</p>
    </div>
  </section>

  <section class="card card-back">
    <div class="contact">
      <h1 class="doctor-name">Dr. Bram Tovelund, D.C.</h1>
      <ul class="contact-list">
        <li>
          <svg viewBox="0 0 12 12"><circle cx="6" cy="6" r="6" fill="#ff8000"/><path d="M4 3.2l1.2 1.4-.6.8c.4.9 1 1.5 1.9 1.9l.8-.6L8.8 8c-.3.6-.8.9-1.4.8C5.4 8.4 3.6 6.6 3.2 4.6c-.1-.6.2-1.1.8-1.4z" fill="#fff"/></svg>
          971.386.4217
        </li>
        <li>
          <svg viewBox="0 0 12 12"><circle cx="6" cy="6" r="6" fill="#ff8000"/><rect x="3" y="4" width="6" height="4.2" fill="none" stroke="#fff" stroke-width=".9"/><path d="M3 4l3 2.3L9 4" fill="none" stroke="#fff" stroke-width=".9"/></svg>
          b.tovelund@FreshStrideHealth.com
        </li>
        <li>
          <svg viewBox="0 0 12 12"><circle cx="6" cy="6" r="6" fill="#ff8000"/><circle cx="6" cy="6" r="3" fill="none" stroke="#fff" stroke-width=".8"/><path d="M3 6h6M6 3c-1.4 1.6-1.4 4.4 0 6M6 3c1.4 1.6 1.4 4.4 0 6" fill="none" stroke="#fff" stroke-width=".7"/></svg>
          www.BirchValeCare.com
        </li>
      </ul>
      <div class="clinic">
        <p class="clinic-title">Cedar Chiropractic- Alder Bend</p>
        <p>20418 NW Harlow Road, Suite 4</p>
        <p>Alder Bend, OR 97412</p>
        <div class="clinic-rule"></div>
        <p class="clinic-title">Cedar Chiropractic- Fernwick</p>
        <p>13529 SE Marston Street</p>
        <p>Fernwick OR 97358</p>
      </div>
    </div>
    <svg class="corner-band" viewBox="0 0 190 100" aria-hidden="true">
      <polygon points="0,100 190,100 190,18 0,62" fill="#ff8000"/>
    </svg>
  </section>
</body>
</html>
```